Coffee House With Cycling Theme Wants Business Cards

We want to create a business card for a coffee house that has a cycling theme. We expect to use the current logo on one side of the business card and we have been considering adding the words 'COFFEE HOUSE' underneath (see example). For the other side of the business card we want an interesting design with tag-line, address and social media links (the normal business card stuff). See examples provided but we are not fixed on having it exactly as shown, we are very open to great creative ideas. Please note our logo has the initials ‘RM' in orange embedded in the design and this must be retained. However, you can play with the words COFFEE HOUSE as well as use the orange color on the backside of the business card, as you see fit. For an image on the backside of the business card it can be a photo, hand-drawn or whatever but it must visually combine coffee and cycling in some way. The interior of the Coffee House will be reclaimed wood, rustic and have an urban feel to it with cycling artifacts hanging from the walls/ceiling, etc. Finally, it would be beneficial if the business card design elements can be easily used on flyers and other promotional assets. Good luck, we are looking forward to seeing your creative ideas.

Target Market(s)

Coffee lovers and cycling fans

Contact Information for Business Card

See project description.

Colors

Designer to choose colors to be used in the design.

Requirements
Must have
• Must use the current logo provided and combine a coffee and bike theme.
Nice to have
• Orange is used in current logo and could be used as an accent color on the backside of the business card.

```html
<!DOCTYPE html>
<html lang="en">
<head>
<meta charset="utf-8">
<title>RM Coffee House – Business Card</title>
<link href="https://fonts.googleapis.com/css2?family=Lato:wght@400;700&display=swap" rel="stylesheet">
<style>
  :root {
    --bg: #5a5a5a;
    --card-light: #eeeeee;
    --charcoal: #3d3d3d;
    --orange: #ff6a1f;
    --ink: #333333;
    --white: #ffffff;
    --bean-dark: #3b2416;
    --bean-mid: #7a4a2c;
    --sand: #b88a62;
    --road: #2c2a29;
  }
  * { margin: 0; padding: 0; box-sizing: border-box; }
  html, body { width: 1200px; height: 1200px; overflow: hidden; }
  body {
    background: var(--bg);
    font-family: "Lato", sans-serif;
    position: relative;
  }
  .card {
    position: absolute;
    top: 310px;
    height: 594px;
    overflow: hidden;
  }
  .card-front { left: 234px; width: 364px; background: var(--card-light); }
  .card-back { left: 627px; width: 370px; }

  .brand {
    height: 363px;
    display: flex;
    flex-direction: column;
    align-items: center;
  }
  .brand-mark {
    margin-top: 88px;
    display: flex;
    align-items: center;
    gap: 14px;
    height: 130px;
  }
  .brand-initials {
    font-size: 120px;
    font-weight: 700;
    color: var(--orange);
    line-height: 1;
    letter-spacing: 2px;
  }
  .brand-dot {
    width: 26px; height: 26px;
    border-radius: 50%;
    background: var(--charcoal);
  }
  .brand-name {
    margin-top: 22px;
    font-size: 36px;
    font-weight: 400;
    color: var(--orange);
    line-height: 1;
  }
  .brand-web {
    margin-top: 20px;
    font-size: 19px;
    color: var(--ink);
    line-height: 1;
  }
  .tagline-band {
    height: 113px;
    background: var(--charcoal);
    text-align: center;
    padding-top: 27px;
  }
  .tagline-title {
    font-size: 33px;
    font-weight: 700;
    color: var(--orange);
    line-height: 1;
  }
  .tagline-sub {
    margin-top: 9px;
    font-size: 19px;
    font-weight: 700;
    color: var(--white);
    line-height: 1;
  }
  .address-band {
    height: 118px;
    background: var(--orange);
    color: var(--white);
    text-align: center;
    font-size: 18px;
    font-weight: 700;
    line-height: 24px;
    padding-top: 28px;
  }

  .back-scene {
    position: absolute; inset: 0;
    background: linear-gradient(180deg,
      var(--bean-dark) 0%, var(--bean-mid) 25%, #a97650 42%,
      #8a5d3d 55%, var(--sand) 68%, #6f5040 75%, var(--road) 82%, var(--road) 100%);
  }
  .social {
    position: absolute;
    left: 284px;
    top: 499px;
    transform: translateX(-50%);
    display: flex;
    flex-direction: column;
    align-items: center;
  }
  .social-icons {
    display: flex;
    gap: 6px;
  }
  .social-dot {
    width: 36px; height: 36px;
    border-radius: 50%;
    background: var(--white);
  }
  .social-handle {
    margin-top: 11px;
    font-size: 21px;
    color: var(--white);
    line-height: 1;
    white-space: nowrap;
  }
</style>
</head>
<body>
  <section class="card card-front">
    <div class="brand">
      <div class="brand-mark">
        <span class="brand-initials">RM</span>
        <span class="brand-dot"></span>
      </div>
      <div class="brand-name">COFFEE HOUSE</div>
      <div class="brand-web">www.rmcoffeehouse.com</div>
    </div>
    <div class="tagline-band">
      <div class="tagline-title">BEANS &amp; BIKES</div>
      <div class="tagline-sub">GET YOUR DAILY QUOTA</div>
    </div>
    <div class="address-band">
      501, Address Goes Here<br>Country Name, 123456
    </div>
  </section>

  <section class="card card-back">
    <div class="back-scene" role="img" aria-label="Photo montage: roasted coffee beans above a steaming white cup of coffee that merges into a desert road stretching into the distance"></div>
    <div class="social">
      <div class="social-icons">
        <span class="social-dot"></span>
        <span class="social-dot"></span>
      </div>
      <span class="social-handle">rmcoffeehouse</span>
    </div>
  </section>
</body>
</html>
```